Cell Tower company needs website updated

We need a website that does not look like it was designed in the early 1990's. The company fabricates, installs and reinforces communication towers throughout the US, Caribbean, Central and S. America. We are located in Pensacola Florida. Our tower technicians travel to wherever the work is. I have some good pictures taken from towers to use on the site. I want the site to reflect the excitement that the wireless communication industry has. I want to the company to look exciting and attract new employees. The majority of our business is modifying and reinforcing existing cell towers to accept all the new tower top antennas that the increasing wireless mobile world demands.
Updates

I have added some sample photos from our business to our ArtBazaar profile.

We are now going through each design to find what is most suitable for our needs. Thank you all for your time in this matter.

Industry/Entity Type

Wireless Communication

```html
<!DOCTYPE html>
<html lang="en">
<head>
<meta charset="utf-8">
<title>TowerCraft Incorporated</title>
<link href="https://fonts.googleapis.com/css2?family=Open+Sans:wght@400;600&display=swap" rel="stylesheet">
<style>
:root{
  --red:#d4201a;
  --red-dark:#8a0c0c;
  --maroon:#7a0a0a;
  --ink:#222;
  --text:#333;
  --footer:#000;
  --white:#fff;
  --rule:#bbb;
}
*{margin:0;padding:0;box-sizing:border-box}
html,body{width:1152px;height:1200px;overflow:hidden;background:var(--white);font-family:"Open Sans",sans-serif;color:var(--text)}
.page{position:relative;width:1152px;height:1200px}
.abs{position:absolute}

.brand{left:134px;top:40px}
.brand-name{font-size:38px;font-weight:400;color:var(--ink);letter-spacing:-0.5px;display:flex;align-items:center;gap:8px}
.brand-mark{width:12px;height:12px;background:var(--red);border-radius:50%}
.brand-sub{font-size:7px;letter-spacing:2px;text-align:right;color:var(--ink);margin-top:-2px}

.nav-band{left:702px;top:110px;width:326px;height:36px;background:linear-gradient(#e2261c,#c81812)}
.nav-fold{left:670px;top:110px}
.nav-bar{left:124px;top:142px;width:546px;height:36px;background:linear-gradient(#e2261c,#c81812);display:flex;align-items:center;padding-left:16px}
.nav-item{color:var(--white);font-size:14.5px;padding:0 14px;height:27px;line-height:27px;margin-right:6px}
.nav-item.is-active{background:var(--white);color:var(--red)}
.tower-art{left:812px;top:12px;width:108px;height:172px;background:linear-gradient(#f08a2a 0%,#e03a2a 30%,#f7d5d5 100%);opacity:.55;border-radius:6px}
.hero-line{left:124px;top:190px;width:904px;height:1px;background:var(--red)}

.dropdown{left:329px;top:174px;width:113px;background:#f4f4f4;box-shadow:0 2px 3px rgba(0,0,0,.25)}
.dropdown-item{height:20px;font-size:11px;color:var(--red);display:flex;align-items:center;gap:8px;padding-left:6px;border-bottom:1px solid #ddd}
.dropdown-item svg{width:7px;height:8px}

.hero-shadow{left:60px;top:440px;width:1032px;height:90px;background:radial-gradient(ellipse at center,rgba(0,0,0,.14),rgba(0,0,0,0) 70%)}
.hero{left:124px;top:191px;width:904px;height:298px;background:linear-gradient(100deg,#6a6a5a 0%,#4a7bc2 25%,#5a4a3a 42%,#8a8a8a 60%,#9fc0e4 80%,#c6daf0 100%)}
.dots{left:552px;top:492px;display:flex;gap:4px}
.dot{width:8px;height:8px;border-radius:50%;background:var(--red)}
.dot.is-current{background:var(--white);box-shadow:0 0 2px #999}

.feature-title{font-size:21px;color:var(--maroon)}
.feature-text{font-size:9.5px;line-height:11px;text-align:justify;width:151px;color:var(--ink)}
.feature-more{font-size:9.5px;color:var(--red);text-decoration:underline}
.feature-art{background:linear-gradient(#cfcfcf,#555);opacity:.7;border-radius:4px}
.divider{width:1px;height:84px;background:var(--rule);top:557px}

.welcome-title{left:138px;top:704px;font-size:20px;color:var(--maroon)}
.welcome-text{left:150px;top:742px;width:498px;font-size:10px;line-height:11.6px;text-align:justify;color:var(--ink)}

.updates-head{left:862px;top:708px;width:166px;height:35px;background:var(--red-dark);color:var(--white);font-size:15px;font-weight:600;display:flex;align-items:center;justify-content:center}
.updates-notch{left:855px;top:718px;width:0;height:0;border-top:8px solid transparent;border-bottom:8px solid transparent;border-right:8px solid var(--red-dark)}
.news{left:866px;width:162px}
.news-title{font-size:11.5px;color:var(--maroon);text-decoration:underline;margin-bottom:3px}
.news-text{font-size:9.5px;line-height:11.6px;text-align:justify;color:var(--text);padding-left:1px}
.news-more{text-align:right;font-size:10px;color:var(--maroon);text-decoration:underline;margin-top:6px}
.news-rule{margin:4px 12px 0 8px;height:1px;background:var(--ink)}

.footer{left:0;top:1070px;width:1152px;height:130px;background:var(--footer)}
.footer-col{top:1078px;list-style:none}
.footer-col li{font-size:10px;color:var(--white);height:19.2px}
.footer-col li.is-active{color:var(--red);text-decoration:underline}
.follow{left:854px;top:1097px;height:20px;background:var(--red-dark);color:var(--white);font-size:11.5px;display:flex;align-items:center;padding:0 9px}
.follow-tip{left:934px;top:1097px;width:0;height:0;border-top:10px solid transparent;border-bottom:10px solid transparent;border-left:7px solid var(--red-dark)}
.social{top:1099px;width:16px;height:16px;background:var(--white);border-radius:2px}
.copyright{left:0;top:1184px;width:1070px;text-align:center;font-size:9.5px;color:var(--white)}
</style>
</head>
<body>
<div class="page">

  <div class="abs brand">
    <div class="brand-name"><span class="brand-mark"></span>TowerCraft</div>
    <div class="brand-sub">INCORPORATED</div>
  </div>

  <div class="abs nav-band"></div>
  <svg class="abs nav-fold" width="32" height="68" viewBox="0 0 32 68"><polygon points="0,32 32,0 32,36 0,68" fill="#8a0c0c"/></svg>
  <div class="abs tower-art" role="img" aria-label="Red communication tower with orange signal waves"></div>

  <nav class="abs nav-bar">
    <span class="nav-item is-active">HOME</span>
    <span class="nav-item">ABOUT US</span>
    <span class="nav-item is-active" style="margin-left:6px">SERVICES</span>
    <span class="nav-item">WORKS</span>
    <span class="nav-item">CONTACT US</span>
  </nav>

  <div class="abs hero-shadow"></div>
  <div class="abs hero-line"></div>
  <div class="abs hero" role="img" aria-label="Collage of tower technicians climbing, welding and working on steel towers against blue sky and sunset"></div>

  <div class="abs dropdown">
    <div class="dropdown-item"><svg viewBox="0 0 7 8"><path d="M1 0l5 4-5 4z" fill="#8a0c0c"/></svg>Service # 1</div>
    <div class="dropdown-item"><svg viewBox="0 0 7 8"><path d="M1 0l5 4-5 4z" fill="#8a0c0c"/></svg>Service # 1</div>
    <div class="dropdown-item"><svg viewBox="0 0 7 8"><path d="M1 0l5 4-5 4z" fill="#8a0c0c"/></svg>Service # 1</div>
    <div class="dropdown-item" style="background:#e4e4e4"><svg viewBox="0 0 7 8"><path d="M1 0l5 4-5 4z" fill="#8a0c0c"/></svg>Service # 1</div>
  </div>

  <div class="abs dots"><span class="dot"></span><span class="dot is-current"></span><span class="dot"></span></div>

  <!-- Features -->
  <div class="abs feature-art" style="left:148px;top:556px;width:68px;height:82px" role="img" aria-label="Fountain pen writing a flourish"></div>
  <div class="abs" style="left:222px;top:553px">
    <div class="feature-title">Testimonial</div>
    <p class="feature-text" style="margin-top:2px">Lorem Ipsum is simply dummy text of the printing and typesetting industry.</p>
  </div>
  <div class="abs feature-more" style="left:323px;top:629px">ReadMore..</div>
  <div class="abs divider" style="left:407px"></div>

  <div class="abs feature-art" style="left:422px;top:570px;width:104px;height:56px" role="img" aria-label="Handshake silhouette"></div>
  <div class="abs" style="left:533px;top:553px">
    <div class="feature-title">Opportunity</div>
    <p class="feature-text" style="margin-top:2px">Lorem Ipsum is simply dummy text of the printing and typesetting industry.</p>
  </div>
  <div class="abs feature-more" style="left:638px;top:629px">ReadMore..</div>
  <div class="abs divider" style="left:716px"></div>

  <svg class="abs" style="left:732px;top:554px" width="92" height="92" viewBox="0 0 92 92"><circle cx="46" cy="46" r="44" fill="#e0b020"/></svg>
  <div class="abs" style="left:827px;top:553px">
    <div class="feature-title">QualityWork</div>
    <p class="feature-text" style="margin-top:2px">Lorem Ipsum is simply dummy text of the printing and typesetting industry.</p>
  </div>
  <div class="abs feature-more" style="left:933px;top:629px">ReadMore..</div>

  <!-- Welcome -->
  <h1 class="abs welcome-title" style="font-weight:400">Welcome To TowerCraft!!</h1>
  <p class="abs welcome-text">Lorem Ipsum is simply dummy text of the printing and typesetting industry. Lorem Ipsum has been the industry's standard dummy text ever since the 1500s, when an unknown printer took a galley of type and scrambled it to make a type specimen book. It has survived not only five centuries, but also the leap into electronic typesetting, remaining essentially unchanged. It was popularised in the 1960s with the release of Letraset sheets containing Lorem Ipsum passages, and more recently with desktop publishing software like Aldus PageMaker including versions of Lorem Ipsum.</p>

  <!-- Updates -->
  <div class="abs updates-notch"></div>
  <div class="abs updates-head">Latest Updates</div>
  <div class="abs news" style="top:753px">
    <div class="news-title">News#1</div>
    <p class="news-text">Lorem Ipsum is simply dummy text of the printing and typesetting industry.</p>
    <div class="news-more">ReadMore . .</div>
    <div class="news-rule"></div>
  </div>
  <div class="abs news" style="top:840px">
    <div class="news-title">News#1</div>
    <p class="news-text">Lorem Ipsum is simply dummy text of the printing and typesetting industry.</p>
    <div class="news-more">ReadMore . .</div>
    <div class="news-rule"></div>
  </div>

  <!-- Footer -->
  <footer class="abs footer"></footer>
  <ul class="abs footer-col" style="left:133px">
    <li class="is-active">HOME</li><li>ABOUT US</li><li>SERVICES</li><li>WORKS</li><li>CONTACT US</li>
  </ul>
  <ul class="abs footer-col" style="left:223px">
    <li>TESTIMONIAL</li><li>OPPORTUNITY</li><li>QUALITYWORK</li><li>TERMS &amp; CONDITIONS</li>
  </ul>
  <div class="abs follow">FOLLOW US</div>
  <div class="abs follow-tip"></div>
  <div class="abs social" style="left:948px" aria-label="Social link"></div>
  <div class="abs social" style="left:971px" aria-label="Social link"></div>
  <div class="abs social" style="left:997px" aria-label="Social link"></div>
  <div class="abs copyright">copyright all roghts resevered - 2014</div>

</div>
</body>
</html>
```